Poster design for "A Frame" Sign

I need a design for an A Frame sign. Measurements and Specifications here:
http://www.brodexsupply.com.au/pg/a-boards/ABPBBLKPRT-Print-Specs.pdf

Actually, it will need to be two designs, one with an arrow pointing left and one with an arrow pointing right, otherwise exactly the same.

LOGO to be used is attached. Colours of design should match logo and should also include orange tones.

The A Frame sign is to be put on the driveway of my home studio at a main road in a residential suburban area. Cars drive by at around 50 km/h, so there needs to be an eye catcher that there is a nurturing home massage studio here.

Logo can be left or right, somehow incorporated into the text below:
-
[Big header, ideally "LeHavre" font]
Tarova Calm
Massage Studio

[slightly smaller font, serif, with bullet points]
- Relaxation Massage
- Remedial Massage
- Pregnancy Massage
- Kahuna Massage

[big Arrow to the left/right - one for each side of the frame]

[sans serif font, same size as above]
Bookings essential!
ph 0491 857 604
www.tarovacalm.com.au

[serif font, same as above]
EFTPOS and instant health fund claims available.
-

Residential

f37022

```html
<!DOCTYPE html>
<html lang="en">
<head>
<meta charset="utf-8">
<title>Gentle Haven – A-Frame Sign Board</title>
<link rel="stylesheet" href="https://fonts.googleapis.com/css2?family=Josefin+Sans:wght@700&family=Varela+Round&family=PT+Sans+Narrow&display=swap">
<style>
  :root {
    --backdrop: #cbcecf;
    --label-ink: #1f1f1f;
    --brand-pink: #ee4593;
    --brand-rim: #d8195e;
    --sun-yellow: #fdd886;
    --emblem-plum: #9c1645;
    --emblem-rose: #e23f7f;
    --ink-white: #ffffff;
  }
  * { margin: 0; padding: 0; box-sizing: border-box; }
  html, body {
    width: 979px;
    height: 1200px;
    overflow: hidden;
    background: var(--backdrop);
  }
  .presentation {
    position: relative;
    width: 979px;
    height: 1200px;
  }
  .presentation-title {
    position: absolute;
    left: 40px;
    top: 214px;
    font-family: "PT Sans Narrow", sans-serif;
    font-size: 26px;
    font-weight: 400;
    color: var(--label-ink);
    letter-spacing: 0.3px;
  }
  .sign-board {
    position: absolute;
    top: 290px;
    width: 430px;
    height: 637px;
    display: block;
  }
  .sign-board--left { left: 40px; }
  .sign-board--right { left: 509px; }

  .board-ground { fill: var(--sun-yellow); }
  .board-halo { fill: var(--brand-pink); stroke: var(--brand-rim); stroke-width: 5; }
  .booking-band { fill: var(--brand-pink); }
  .brand-name {
    font-family: "Josefin Sans", sans-serif;
    font-weight: 700;
    font-size: 66px;
    fill: var(--ink-white);
  }
  .service-item {
    font-family: "Varela Round", sans-serif;
    font-size: 24px;
    fill: var(--ink-white);
  }
  .service-bullet-ring { fill: none; stroke: var(--ink-white); stroke-width: 1.8; }
  .service-bullet-dot { fill: var(--ink-white); }
  .booking-note {
    font-family: "PT Sans Narrow", sans-serif;
    font-size: 25px;
    fill: var(--ink-white);
  }
  .direction-ring { fill: none; stroke: var(--ink-white); stroke-width: 2.5; }
  .direction-arrow { fill: none; stroke: var(--ink-white); stroke-width: 3.5; stroke-linecap: round; stroke-linejoin: round; }
  .emblem-area { fill: url(#emblemTone); stroke: var(--emblem-plum); stroke-width: 3; }
</style>
</head>
<body>
<main class="presentation">
  <h1 class="presentation-title">GENTLE HAVEN “A” Sign Board</h1>

  <!-- Left-facing board: arrow points right -->
  <svg class="sign-board sign-board--left" viewBox="0 0 377 558" aria-label="Gentle Haven sign board, arrow pointing right">
    <defs>
      <radialGradient id="emblemTone" cx="0.45" cy="0.5" r="0.6">
        <stop offset="0" stop-color="#f06aa3"/>
        <stop offset="1" stop-color="#a3184c"/>
      </radialGradient>
      <clipPath id="boardClipLeft"><rect width="377" height="558"/></clipPath>
    </defs>
    <g clip-path="url(#boardClipLeft)">
      <rect class="board-ground" width="377" height="558"/>
      <circle class="board-halo" cx="140" cy="130" r="270"/>
      <rect class="booking-band" x="0" y="415" width="377" height="129"/>
    </g>

    <text class="brand-name" x="33" y="90" textLength="307" lengthAdjust="spacingAndGlyphs">GENTLE</text>
    <text class="brand-name" x="33" y="147" textLength="307" lengthAdjust="spacingAndGlyphs">HAVEN</text>

    <g class="service-list">
      <circle class="service-bullet-ring" cx="44" cy="196" r="6"/><circle class="service-bullet-dot" cx="44" cy="196" r="2.8"/>
      <text class="service-item" x="67" y="204">Relaxation Massage</text>
      <circle class="service-bullet-ring" cx="44" cy="230" r="6"/><circle class="service-bullet-dot" cx="44" cy="230" r="2.8"/>
      <text class="service-item" x="67" y="238">Remedial Massage</text>
      <circle class="service-bullet-ring" cx="44" cy="264" r="6"/><circle class="service-bullet-dot" cx="44" cy="264" r="2.8"/>
      <text class="service-item" x="67" y="272">Pregnancy Massage</text>
      <circle class="service-bullet-ring" cx="44" cy="297" r="6"/><circle class="service-bullet-dot" cx="44" cy="297" r="2.8"/>
      <text class="service-item" x="67" y="305">Kahuna Massage</text>
    </g>

    <circle class="emblem-area" cx="83" cy="480" r="63" role="img" aria-label="Brand illustration area: stylised woman in profile with swirling hair"/>

    <text class="booking-note" x="170" y="476">Bookings</text>
    <text class="booking-note" x="170" y="500">essential!</text>

    <circle class="direction-ring" cx="313" cy="480" r="43"/>
    <path class="direction-arrow" d="M287 480 H338 M318 460 L338 480 L318 500"/>
  </svg>

  <!-- Right-facing board: arrow points left -->
  <svg class="sign-board sign-board--right" viewBox="0 0 377 558" aria-label="Gentle Haven sign board, arrow pointing left">
    <defs>
      <clipPath id="boardClipRight"><rect width="377" height="558"/></clipPath>
    </defs>
    <g clip-path="url(#boardClipRight)">
      <rect class="board-ground" width="377" height="558"/>
      <circle class="board-halo" cx="237" cy="130" r="270"/>
      <rect class="booking-band" x="0" y="413" width="377" height="129"/>
    </g>

    <text class="brand-name" x="43" y="90" textLength="307" lengthAdjust="spacingAndGlyphs">GENTLE</text>
    <text class="brand-name" x="43" y="147" textLength="307" lengthAdjust="spacingAndGlyphs">HAVEN</text>

    <g class="service-list">
      <circle class="service-bullet-ring" cx="87" cy="194" r="6"/><circle class="service-bullet-dot" cx="87" cy="194" r="2.8"/>
      <text class="service-item" x="108" y="202">Relaxation Massage</text>
      <circle class="service-bullet-ring" cx="87" cy="228" r="6"/><circle class="service-bullet-dot" cx="87" cy="228" r="2.8"/>
      <text class="service-item" x="108" y="236">Remedial Massage</text>
      <circle class="service-bullet-ring" cx="87" cy="262" r="6"/><circle class="service-bullet-dot" cx="87" cy="262" r="2.8"/>
      <text class="service-item" x="108" y="270">Pregnancy Massage</text>
      <circle class="service-bullet-ring" cx="87" cy="295" r="6"/><circle class="service-bullet-dot" cx="87" cy="295" r="2.8"/>
      <text class="service-item" x="108" y="303">Kahuna Massage</text>
    </g>

    <circle class="direction-ring" cx="63" cy="477" r="43"/>
    <path class="direction-arrow" d="M89 477 H38 M58 457 L38 477 L58 497"/>

    <text class="booking-note" x="118" y="473">Bookings</text>
    <text class="booking-note" x="118" y="497">essential!</text>

    <circle class="emblem-area" cx="295" cy="477" r="63" role="img" aria-label="Brand illustration area: stylised woman in profile with swirling hair"/>
  </svg>
</main>
</body>
</html>
```